Business Card Design

Buy and sell properties
Buy and rehab properties
Buy properties for cash
That is what I do but do need a logo
looking for some type of logo or design on it
Just started business
Back of card should say something like BUY HOUSES CASH
Overview: it is a new company. Basically I buy properties wholesale and fix them up and sell them or sell them to other fix and flippers
Background: company is new so not any background
Market: is basically anyone selling a house or buying a house. Someone that needs to sell house fast. Basically I am a cash home buyer!!!

Updates
Email on card should be:   harborlanerealtyinc@mailbox.test

Industry/Entity Type
House
Contact Information for Business Card
Harbor Lane Realty Inc
PO Box 718269
Cedar Marsh FL 32987

Dale Morrick
dmorrick@mailbox.test
555-271-6094

```html
<!DOCTYPE html>
<html lang="en">
<head>
<meta charset="utf-8">
<title>Harbor Lane Realty Inc — Business Card</title>
<link href="https://fonts.googleapis.com/css2?family=Tinos:wght@400;700&display=swap" rel="stylesheet">
<style>
  :root {
    --page: #eceae6;
    --white: #ffffff;
    --blue: #2377b6;
    --grey: #777777;
    --ink: #1d1d1f;
    --shadow: rgba(0,0,0,0.22);
  }
  * { box-sizing: border-box; margin: 0; padding: 0; }
  html, body { width: 1200px; height: 848px; overflow: hidden; background: var(--page); }
  body { position: relative; font-family: "Tinos", "Times New Roman", serif; }

  .card {
    position: absolute;
    width: 560px;
    height: 320px;
    box-shadow: 0 10px 24px var(--shadow);
    overflow: hidden;
  }
  .card-front { left: 50px; top: 90px; background: var(--white); }
  .card-back {
    left: 590px; top: 438px;
    background: linear-gradient(150deg, var(--blue) 0%, #4f7aa3 35%, #6f7a86 65%, var(--grey) 100%);
  }

  .front-shapes { position: absolute; inset: 0; }

  .brand {
    position: absolute;
    left: 30px; top: 130px;
    width: 250px;
    display: flex; align-items: center; gap: 12px;
  }
  .brand-mark {
    width: 30px; height: 30px; border-radius: 50%;
    background: var(--blue); flex: none;
  }
  .brand-name {
    font-size: 25px; font-weight: 700; color: var(--ink);
    line-height: 1.1;
  }

  .holder-name {
    position: absolute; right: 30px; top: 30px;
    color: var(--white); font-size: 18px;
  }

  .contact {
    position: absolute; right: 24px; bottom: 42px;
    list-style: none; text-align: right; color: var(--white);
    font-size: 14px; line-height: 1.6;
  }
  .contact li { display: flex; justify-content: flex-end; align-items: center; gap: 8px; }
  .contact svg { width: 12px; height: 12px; flex: none; }

  .back-company {
    position: absolute; left: 44px; top: 100px;
    color: var(--white); font-size: 26px; letter-spacing: 0.5px;
  }
  .back-tagline {
    position: absolute; right: 48px; top: 190px;
    color: var(--white); font-size: 22px; letter-spacing: 0.5px;
  }
</style>
</head>
<body>
  <section class="card card-front" aria-label="Business card front">
    <svg class="front-shapes" viewBox="0 0 560 320" width="560" height="320" aria-hidden="true">
      <polygon points="225,0 560,0 560,86 295,86" fill="var(--blue)"/>
      <polygon points="300,92 560,92 560,320 330,320" fill="var(--grey)"/>
    </svg>

    <div class="brand">
      <span class="brand-mark"></span>
      <span class="brand-name">Harbor Lane Realty Inc</span>
    </div>

    <p class="holder-name">Dale Morrick</p>

    <ul class="contact">
      <li>555-271-6094
        <svg viewBox="0 0 24 24" aria-hidden="true"><path fill="#fff" d="M6.6 10.8a15 15 0 0 0 6.6 6.6l2.2-2.2c.3-.3.7-.4 1-.2 1.1.4 2.3.6 3.6.6.6 0 1 .4 1 1V20c0 .6-.4 1-1 1A17 17 0 0 1 3 4c0-.6.4-1 1-1h3.5c.6 0 1 .4 1 1 0 1.3.2 2.5.6 3.6.1.3 0 .7-.2 1z"/></svg>
      </li>
      <li>dmorrick@mailbox.test
        <svg viewBox="0 0 24 24" aria-hidden="true"><path fill="#fff" d="M3 5h18v14H3z M4.5 6.5 12 12l7.5-5.5" stroke="#777" stroke-width="1.2"/></svg>
      </li>
      <li>718269 Cedar Marsh FL 32987
        <svg viewBox="0 0 24 24" aria-hidden="true"><path fill="#fff" d="M12 2a7 7 0 0 0-7 7c0 5 7 13 7 13s7-8 7-13a7 7 0 0 0-7-7zm0 9.5a2.5 2.5 0 1 1 0-5 2.5 2.5 0 0 1 0 5z"/></svg>
      </li>
    </ul>
  </section>

  <section class="card card-back" aria-label="Business card back">
    <p class="back-company">Harbor Lane Realty Inc</p>
    <p class="back-tagline">BUY HOUSES CASH</p>
  </section>
</body>
</html>
```